依頼詳細
【Tobiraのサービス特徴はこの3つ!】
●無料で請求書管理
請求書の作成・PDFダウンロードなどの機能はずっと無料でご利用になれます。顧客の数や、請求書の枚数に制限はありません。さらに有料プランなら見積り機能も使えます
●あんしんの印刷・郵送システム
Tobiraでは安全なドキュメントセンターで印刷、封入、封かん、発送を行なっています。それぞれの作業は機械が行うため請求書をの中身を人が見るということや人為的なミスはありません。詳しくはこちら
●どこでも請求書の作成・管理ができる
専用画面からログインすれば、書き方がわからなくてもテンプレートの必要事項を埋めるだけで出張先や自宅、iPad、スマートフォンなどからいつでも作成・編集できます。

---------------------------------------------------------------------------------

今回は、2種類のデザインを採用させていただきます。
1件10万円で、2種類の募集となりますので、
ドド~ンと総額20万円のキャンペーンとなります。
記載項目
■ 希望するデザイン
フリーランスのエンジニアさん、デザイナーさんが使いたくなる、オシャレで格好いい請求書の、オリジナルのデザインをご提案ください。

また、以下内容は請求書面として必要な事項となりますので必ず記載ください。
(現状の請求書のデータをアップロードしておりますので参照・活用ください)
・請求年月日
・請求先名称
・請求元(名前、住所、TEL、FAX、メールアドレス)
・請求元印影画像
・請求金額合計
・請求明細(20行、小計、消費税、合計金額)
・備考欄(3行)
・振込口座欄(1行)
希望イメージ
• +5 0 +5
• シンプル
複雑
• 単色
カラフル
• 暗い
明るい
• 日常
高級
• 遊び心
厳粛
• 未来的
伝統的
• 女性的
男性的
希望する色
色の指定はございません
納品ファイル
• イラストレーター形式 (.ai)
• フォトショップ形式 (.psd)
補足説明
■ 納品ファイルの希望
Illustrator形式、Photoshop形式、Fireworks形式
(最大容量は1024kbとしてそれ以下で作ってください)
依頼公開後の追記内容
■ 選んだ理由

bluewhistlerさんの作品は、どの業種でも使いやすく受け取り手も安心できるデザインということで選ばせて頂きました

もう一点は(http://www.kumoshi-hub.jp/work/proposal/5830417)になります。(現在システムの都合で当選にできていません)
k-atelierさんの作品は請求書のかっちりした感じに少し遊びを加えた感じのバランスがよく、採用しました。

■ 提案者全員のお礼・コメント

これほど多くの応募をいただけるとは思っておらずとても驚くとともに、感謝の気持でいっぱいです。

請求書のデザインということで、単純にデザイン性だけでは判断できず、どれも素敵な作品ばかりだったので選定には本当に時間がかかりました。

今回の当選作品以外にもTobira賞として10点ほど買取のオファーを出させて頂きます。どうぞよろしくおねがいします。

この度は本当にご応募ありがとうございました。

```html
<!DOCTYPE html>
<html lang="ja">
<head>
<meta charset="utf-8">
<title>請求書</title>
<link rel="stylesheet" href="https://fonts.googleapis.com/css2?family=Noto+Sans+JP:wght@400;500;700&display=swap">
<style>
:root{
  --ink:#333;
  --muted:#666;
  --accent:#3a8fd0;
  --band-light:#dff0fb;
  --band-mid:#bfe0f5;
  --head:#cfe6f6;
  --stripe:#eef7fd;
  --rule:#8ec3e8;
  --seal:#d94a5a;
  --paper:#fff;
}
*{margin:0;padding:0;box-sizing:border-box}
html,body{width:849px;height:1200px;overflow:hidden;background:var(--paper)}
body{position:relative;font-family:"Noto Sans JP",sans-serif;color:var(--ink)}
.header-band{position:absolute;left:0;top:0;width:849px;height:112px;
  background:linear-gradient(135deg,var(--band-mid),var(--band-light) 55%,var(--band-mid))}
.title{position:absolute;left:62px;top:52px;font-size:34px;font-weight:500;letter-spacing:22px}
.issue-date{position:absolute;right:24px;top:50px;font-size:16px}
.invoice-no{position:absolute;right:24px;top:118px;font-size:14px;padding-left:8px;border-bottom:1px solid var(--rule)}
.client{position:absolute;left:57px;top:218px;width:360px;font-size:22px;font-weight:500;padding-bottom:8px;border-bottom:1.5px solid var(--ink)}
.lead{position:absolute;left:57px;top:276px;font-size:11px;letter-spacing:3px;color:var(--muted)}
.amount{position:absolute;left:57px;top:306px;width:360px;display:flex;align-items:baseline;border-bottom:1.5px solid var(--ink);padding-bottom:6px}
.amount .label{font-size:17px;width:140px}
.amount .value{font-size:24px;font-weight:500}
.issuer{position:absolute;left:453px;top:222px;font-size:11px;line-height:1.55}
.issuer .name{font-size:16px;font-weight:500;margin-bottom:12px;padding-bottom:4px;border-bottom:1px solid var(--ink);width:250px}
.issuer .contact{margin-top:14px}
.seal{position:absolute;left:736px;top:234px;width:90px;height:90px}
.items{position:absolute;left:57px;top:427px;width:778px;border-collapse:collapse;font-size:12px}
.items th{background:var(--head);font-weight:500;height:29px;border:1px solid var(--rule)}
.items td{height:21.5px;padding:0 8px;border-left:1px solid var(--rule);border-right:1px solid var(--rule)}
.items tbody tr:nth-child(even) td{background:var(--stripe)}
.items tbody tr:last-child td{border-bottom:1px solid var(--rule)}
.col-name{width:509px}.col-qty{width:99px}.col-unit{width:93px}.col-sum{width:77px}
.num{text-align:right}
.summary{position:absolute;left:566px;top:890px;width:269px;border-collapse:collapse;font-size:12px}
.summary td{height:25px;padding:0 8px;border-bottom:1px solid var(--rule)}
.summary .sum-label{width:192px}
.summary .grand td{background:var(--head);font-weight:500}
.notes{position:absolute;left:57px;top:1040px;font-size:11px;line-height:1.9;color:var(--ink)}
.bank{margin-top:6px}
.bank strong{font-weight:500}
</style>
</head>
<body>
<div class="header-band" role="img" aria-label="淡い青の立方体模様の帯"></div>
<h1 class="title">請求書</h1>
<div class="issue-date">2013年05月11日</div>
<div class="invoice-no">請求番号:20130511005</div>

<div class="client">サンプル株式会社 様</div>
<p class="lead">下記のとおりご請求申し上げます。</p>
<div class="amount"><span class="label">ご請求金額</span><span class="value">¥84,000-</span></div>

<div class="issuer">
  <div class="name">ミナトワークス株式会社</div>
  <div>〒450-0002</div>
  <div>愛知県名古屋市中村区</div>
  <div>名駅4丁目8番2号</div>
  <div>カエデビル3F</div>
  <div class="contact">TEL:052-000-4512</div>
  <div>FAX:052-000-4513</div>
  <div>office@minato-works.jp</div>
</div>
<svg class="seal" viewBox="0 0 90 90" role="img" aria-label="社印の印影">
  <rect x="4" y="4" width="82" height="82" rx="6" fill="none" stroke="var(--seal)" stroke-width="4"/>
</svg>

<table class="items">
  <thead><tr><th class="col-name">品番・品名</th><th class="col-qty">数量</th><th class="col-unit">単価</th><th class="col-sum">金額</th></tr></thead>
  <tbody>
    <tr><td>デザイン</td><td class="num">1</td><td class="num">20,000</td><td class="num">20,000</td></tr>
    <tr><td>企画・素材費用</td><td class="num">1</td><td class="num">60,000</td><td class="num">60,000</td></tr>
    <tr><td></td><td></td><td></td><td></td></tr><tr><td></td><td></td><td></td><td></td></tr>
    <tr><td></td><td></td><td></td><td></td></tr><tr><td></td><td></td><td></td><td></td></tr>
    <tr><td></td><td></td><td></td><td></td></tr><tr><td></td><td></td><td></td><td></td></tr>
    <tr><td></td><td></td><td></td><td></td></tr><tr><td></td><td></td><td></td><td></td></tr>
    <tr><td></td><td></td><td></td><td></td></tr><tr><td></td><td></td><td></td><td></td></tr>
    <tr><td></td><td></td><td></td><td></td></tr><tr><td></td><td></td><td></td><td></td></tr>
    <tr><td></td><td></td><td></td><td></td></tr><tr><td></td><td></td><td></td><td></td></tr>
    <tr><td></td><td></td><td></td><td></td></tr><tr><td></td><td></td><td></td><td></td></tr>
    <tr><td></td><td></td><td></td><td></td></tr><tr><td></td><td></td><td></td><td></td></tr>
  </tbody>
</table>

<table class="summary">
  <tr><td class="sum-label">小計</td><td class="num">80,000</td></tr>
  <tr><td class="sum-label">消費税(5%)</td><td class="num">4,000</td></tr>
  <tr class="grand"><td class="sum-label">合計金額</td><td class="num">84,000</td></tr>
</table>

<div class="notes">
  <div>サンプル(備考欄1行目)</div>
  <div>サンプル(備考欄2行目)</div>
  <div>お振込み手数料は御社ご負担にてお願いします。</div>
  <div class="bank"><strong>お振込先</strong></div>
  <div>みどり信用銀行 本町支店 普通口座 7654321 ミナトワークス(カ</div>
</div>
</body>
</html>
```